QM Studios needs and Interior Design Business card

I can do anything from Commercial to Residential and Free lance. Beginning to end in design selection process.
Need something to catch the eye of potential customers and vendors. From furniture to Tile and Cabinet selections. I can do it all.

Industry/Entity Type

Design Agency

Contact Information for Business Card

QM Studios- Design Consultanting Residential, Commerical
Maybe a cool detail background. Wall paper print that can have some texture

Font styles to use
Serif

Colors
709dcb
34a6d7
b868aa
e667a6
f59296
85acd3
ffffff
000000
5c5c5c

Requirements
Must have
• Square or Rectangular with Rounded edges
• Name
• Address
• Phone
• Email
Nice to have
• Some colored edges More simples not too busy
• Pattern detail in background.
Should not have
• Not too much color

```html
<!DOCTYPE html>
<html lang="en">
<head>
<meta charset="utf-8">
<title>QM Studios – Business Card</title>
<link href="https://fonts.googleapis.com/css2?family=Open+Sans:wght@400;700&display=swap" rel="stylesheet">
<style>
  :root {
    --stage: #e9e9e9;
    --card-black: #0b0b0b;
    --card-black-edge: #1c1c1c;
    --card-white: #f4f5f4;
    --pattern-tone: #dcdedc;
    --ink: #111111;
    --ink-light: #ffffff;
    --ink-muted: #cfcfcf;
    --rule: #3a3a3a;
    --shadow: rgba(0,0,0,0.18);
  }
  * { box-sizing: border-box; margin: 0; padding: 0; }
  html, body {
    width: 1200px; height: 900px; overflow: hidden;
    background: var(--stage);
    font-family: "Open Sans", Arial, sans-serif;
  }
  .canvas { position: relative; width: 1200px; height: 900px; }

  .card {
    position: absolute; left: 300px; width: 600px; height: 343px;
    border-radius: 10px; overflow: hidden;
    box-shadow: 0 6px 18px var(--shadow);
  }

  /* Back of card */
  .card--back { top: 85px; background: var(--card-white); }
  .card--back .pattern-field {
    position: absolute; inset: 0;
    background: linear-gradient(135deg, var(--pattern-tone), #e7e9e7);
  }
  .card--back .brand {
    position: absolute; left: 0; right: 0; top: 72px;
    display: flex; flex-direction: column; align-items: center;
  }
  .brand__circle {
    width: 92px; height: 92px; border-radius: 50%;
    border: 3px solid var(--ink); background: var(--card-white);
  }
  .card--back .brand__name {
    margin-top: 14px; font-size: 26px; letter-spacing: 6px;
    color: var(--ink); font-weight: 400;
  }
  .card--back .tagline {
    position: absolute; left: 0; right: 0; top: 258px; text-align: center;
    font-size: 15px; font-weight: 700; color: var(--ink);
  }

  /* Front of card */
  .card--front {
    top: 470px;
    background: radial-gradient(ellipse at 40% 40%, var(--card-black-edge), var(--card-black) 70%);
    color: var(--ink-light);
  }
  .person { position: absolute; left: 40px; top: 120px; }
  .person__name { font-size: 20px; font-weight: 700; line-height: 1.1; }
  .person__role { font-size: 14px; color: var(--ink-muted); }
  .card--front .brand {
    position: absolute; right: 40px; top: 34px;
    display: flex; flex-direction: column; align-items: center;
  }
  .card--front .brand__circle {
    width: 84px; height: 84px; border: 2px solid var(--ink-light);
    background: transparent;
  }
  .card--front .brand__name {
    margin-top: 10px; font-size: 30px; letter-spacing: 7px; font-weight: 400;
  }
  .divider {
    position: absolute; left: 40px; right: 40px; top: 180px;
    height: 1px; background: var(--rule);
  }
  .contact {
    position: absolute; right: 40px; top: 196px;
    list-style: none; text-align: right; font-size: 15px; line-height: 1.45;
  }
  .contact li { display: flex; justify-content: flex-end; align-items: center; gap: 8px; }
  .contact .icon { width: 12px; height: 12px; fill: var(--ink-light); }
  .contact .spacer { width: 12px; }
</style>
</head>
<body>
<main class="canvas">

  <section class="card card--back">
    <div class="pattern-field" role="img" aria-label="Faint repeating wallpaper pattern in light grey"></div>
    <div class="brand">
      <div class="brand__circle"></div>
      <p class="brand__name">QM Studios</p>
    </div>
    <p class="tagline">Design Consultanting Residential, Commerical</p>
  </section>

  <section class="card card--front">
    <div class="person">
      <p class="person__name">Daniel Harper</p>
      <p class="person__role">Managing Director</p>
    </div>
    <div class="brand">
      <div class="brand__circle"></div>
      <p class="brand__name">QM Studios</p>
    </div>
    <div class="divider"></div>
    <ul class="contact">
      <li>044-987 654 321 <span class="spacer"></span></li>
      <li>hello@qmstudio.net
        <svg class="icon" viewBox="0 0 24 24" aria-hidden="true"><path d="M6.6 10.8a15 15 0 0 0 6.6 6.6l2.2-2.2a1 1 0 0 1 1-.25 11.4 11.4 0 0 0 3.6.57 1 1 0 0 1 1 1V20a1 1 0 0 1-1 1A17 17 0 0 1 3 4a1 1 0 0 1 1-1h3.5a1 1 0 0 1 1 1c0 1.25.2 2.45.57 3.57a1 1 0 0 1-.25 1z"/></svg>
      </li>
      <li>12345, Address Goes Here
        <svg class="icon" viewBox="0 0 24 24" aria-hidden="true"><path d="M2 5h20v14H2z M2 5l10 8 10-8" fill="none" stroke="#fff" stroke-width="2"/></svg>
      </li>
      <li>Country Name, 123456. <span class="spacer"></span></li>
    </ul>
  </section>

</main>
</body>
</html>
```